Business Card Design Project

We need a business card design for an existing company in Dallas/Fort Worth that is expanding services and re-branding. We are changing the name from Bristow Commercial Cleaning to Kelmont Facility Services. We are expanding from only commercial cleaning to include complete commercial landscape and facility maintenance services, too.

As stated, we offer a package of services that includes landscape, janitorial and facility services, which is largely unique in the industry.

We would like a design that communicates trust/partnership with a professional, corporate image, but not necessarily using the standard white business card. We would like a design that perhaps uses darker blues or perhaps a gray background, but we are open to other ideas. We might also be interested in a double-sided design - maybe with our logo on the back, printed on a gray background?

We will probably stick with the attached logo, but if you've got another inspired idea....

Target Market(s)

Property managers, commercial real estate professionals, corporate executives

Industry/Entity Type

Landscape

Requirements
Should not have
• Not interested in old style fonts.

```html
<!DOCTYPE html>
<html lang="en">
<head>
<meta charset="utf-8">
<title>Kelmont Facility Services – Business Card</title>
<link rel="stylesheet" href="https://fonts.googleapis.com/css2?family=Open+Sans:ital,wght@0,400;0,600;0,700;1,400&family=Jost:wght@400;500;600&display=swap">
<style>
  :root {
    --card-dark: #231f20;
    --band-grey: #404040;
    --band-line: #6a6a6a;
    --brand-orange: #f7931e;
    --ink: #231f20;
    --paper: #ffffff;
    --badge: #fde3c2;
  }
  * { margin: 0; padding: 0; box-sizing: border-box; }
  html, body {
    width: 916px; height: 1200px; overflow: hidden;
    background: var(--paper);
    font-family: "Open Sans", Arial, sans-serif;
  }
  .canvas { position: relative; width: 916px; height: 1200px; }

  .card {
    position: absolute;
    background: var(--card-dark);
    border-radius: 18px;
    overflow: hidden;
    box-shadow: 0 6px 10px rgba(0,0,0,0.25);
  }
  .card--front { left: 96px; top: 95px; width: 710px; height: 425px; }
  .card--back  { left: 93px; top: 663px; width: 711px; height: 426px; }

  .brand { position: absolute; width: 560px; height: 108px; }
  .card--front .brand { left: 103px; top: 26px; }
  .card--back .brand  { left: 77px; top: 27px; }

  .brand__square {
    position: absolute; left: 0; top: 0;
    width: 108px; height: 108px;
    border: 4px solid var(--paper);
  }
  .brand__name {
    color: var(--brand-orange);
    font-weight: 700;
    text-transform: uppercase;
    line-height: 1;
    white-space: nowrap;
  }
  .brand__name-main,
  .brand__name-sub { position: absolute; left: 128px; display: block; }
  .brand__name-main { font-size: 48px; letter-spacing: 6px; }
  .brand__name-sub  { font-size: 33px; letter-spacing: 3px; }

  .card--front .brand__name-main { top: -1px; }
  .card--front .brand__name-sub  { top: 49px; }
  .card--back .brand__name-main  { top: 14px; }
  .card--back .brand__name-sub   { top: 64px; }

  .tagline {
    position: absolute; left: 228px; top: 112px;
    color: var(--brand-orange);
    font-style: italic; font-size: 14px; line-height: 1;
    white-space: nowrap;
  }

  .contact-panel {
    position: absolute; left: 32px; top: 156px;
    width: 644px; height: 269px;
    background: var(--brand-orange);
    border-radius: 14px 14px 0 0;
  }
  .person { position: absolute; left: 35px; top: 28px; }
  .person__name { color: var(--paper); font-weight: 700; font-size: 27px; line-height: 1.1; }
  .person__role { color: var(--ink); font-weight: 700; font-size: 16px; margin-top: 2px; }

  .contact-list { position: absolute; left: 35px; top: 108px; list-style: none; }
  .contact-list li {
    display: flex; align-items: center; gap: 7px;
    height: 28px;
    color: var(--ink); font-weight: 600; font-size: 19px;
  }
  .contact-list__badge {
    width: 20px; height: 22px;
    border-radius: 4px;
    background: var(--badge);
    color: var(--brand-orange);
    font-size: 16px; font-weight: 600;
    display: flex; align-items: center; justify-content: center;
  }
  .website {
    position: absolute; left: 0; right: 0; bottom: 18px;
    text-align: center;
    color: var(--paper); font-weight: 600; font-size: 17px;
  }

  .grey-band {
    position: absolute; left: 0; top: 185px;
    width: 377px; height: 241px;
    background: var(--band-grey);
  }
  .grey-band__lines {
    position: absolute; left: 0; top: 6px; width: 100%; height: 16px;
    border-top: 2px solid var(--band-line);
    border-bottom: 2px solid var(--band-line);
  }
  .services-panel {
    position: absolute; left: 377px; top: 155px;
    width: 295px; height: 271px;
    background: var(--brand-orange);
    border-radius: 14px 14px 0 0;
    padding-top: 40px;
    text-align: center;
    font-family: "Jost", "Century Gothic", sans-serif;
    font-size: 24px; line-height: 30.5px;
    text-transform: uppercase;
  }
  .services-panel .plain { color: var(--ink); font-weight: 400; display: block; }
  .services-panel .strong { color: var(--paper); font-weight: 600; display: block; }
</style>
</head>
<body>
<div class="canvas">

  <section class="card card--front" aria-label="Business card front">
    <div class="brand">
      <div class="brand__square"></div>
      <div class="brand__name">
        <span class="brand__name-main">Kelmont</span>
        <span class="brand__name-sub">Facility Services</span>
      </div>
    </div>
    <p class="tagline">One Source For Landscape, Janitorial and Facility Maintenance</p>

    <div class="contact-panel">
      <div class="person">
        <p class="person__name">Daniel Reyes</p>
        <p class="person__role">Marketing</p>
      </div>
      <ul class="contact-list">
        <li><span class="contact-list__badge">A</span>48 Harlow Ave Cedar Plaza 75201</li>
        <li><span class="contact-list__badge">M</span>06 0517 3382</li>
        <li><span class="contact-list__badge">P</span>(769) 214 3870</li>
        <li><span class="contact-list__badge">E</span>dreyes@kfs.com</li>
      </ul>
      <p class="website">www.kelmontfacilityservices.com</p>
    </div>
  </section>

  <section class="card card--back" aria-label="Business card back">
    <div class="brand">
      <div class="brand__square"></div>
      <div class="brand__name">
        <span class="brand__name-main">Kelmont</span>
        <span class="brand__name-sub">Facility Services</span>
      </div>
    </div>

    <div class="grey-band"><div class="grey-band__lines"></div></div>

    <div class="services-panel">
      <span class="plain">One Source For</span>
      <span class="strong">Landscape</span>
      <span class="strong">Janitorial</span>
      <span class="plain">And</span>
      <span class="strong">Facility</span>
      <span class="strong">Maintenance</span>
    </div>
  </section>

</div>
</body>
</html>
```